Business Card Design Project

A polished, very professional looking business card. I think we want to keep it all grey. I've attached our old logo, and current mockup in which case we really like the font.

Target Market(s)

Target Market are Bride and Grooms and Wedding Coordinators. We are wedding photographers

Industry/Entity Type

Business

Font styles to use
Serif
Sans Serif

Requirements
Must have
• An elegant, yet simple and sophisticated appearance.

Phone number, Email, Website and Social Media link.
Nice to have
• An element that can be spot glossed when printed. Not necessary though.
Should not have
• Bright colors, images or intensive graphics.

```html
<!DOCTYPE html>
<html lang="en">
<head>
<meta charset="utf-8">
<title>Carter Wells Photographers – Business Card</title>
<link rel="stylesheet" href="https://fonts.googleapis.com/css2?family=Cinzel:wght@400;500&family=Arimo:wght@400&display=swap">
<style>
  :root {
    --page: #d6d6d6;
    --card: #404042;
    --card-edge: #2f2f31;
    --ink-light: #f4f4f4;
    --ink-soft: #cfcfcf;
    --band: #d3d3d3;
    --band-ink: #3a3a3c;
    --divider: #9a9a9a;
  }
  * { box-sizing: border-box; margin: 0; padding: 0; }
  html, body {
    width: 1200px; height: 1200px; overflow: hidden;
    background: var(--page);
  }
  .sheet {
    width: 1200px; height: 1200px;
    display: flex; flex-direction: column;
    align-items: center; justify-content: center; gap: 60px;
  }
  .card {
    position: relative;
    width: 900px; height: 514px;
    background: var(--card);
    overflow: hidden;
  }

  /* brand lockup */
  .brand {
    position: absolute;
    display: flex; flex-direction: column; align-items: center;
    color: var(--ink-light);
  }
  .brand-mark {
    width: 52px; height: 52px;
    background: var(--ink-light);
  }
  .brand-rule {
    width: 26px; height: 2px; margin: 16px 0 12px;
    background: var(--ink-light);
  }
  .brand-name {
    font-family: "Cinzel", serif;
    font-weight: 400;
    font-size: 30px;
    letter-spacing: 6px;
    white-space: nowrap;
  }
  .brand-tag {
    margin-top: 6px;
    font-family: "Arimo", sans-serif;
    font-size: 10px;
    letter-spacing: 7px;
    white-space: nowrap;
  }

  .card-front .brand {
    left: 0; right: 0; top: 168px;
  }

  /* back */
  .card-back .brand {
    left: 60px; width: 360px; top: 118px;
  }
  .divider {
    position: absolute; left: 468px; top: 70px;
    width: 2px; height: 260px;
    background: linear-gradient(to bottom, transparent, var(--divider) 40%, var(--divider) 60%, transparent);
  }
  .contact-list {
    position: absolute; left: 510px; top: 86px;
    list-style: none;
    font-family: "Arimo", sans-serif;
    font-size: 17px;
    color: var(--ink-soft);
  }
  .contact-list li {
    display: flex; align-items: center; gap: 22px;
    height: 41px;
  }
  .contact-icon {
    width: 18px; height: 18px; flex: none;
  }
  .band {
    position: absolute; left: 0; bottom: 0;
    width: 900px; height: 120px;
  }
  .tagline {
    position: absolute; left: 40px; top: 418px;
    font-family: "Cinzel", serif;
    font-weight: 500;
    font-size: 15.5px;
    letter-spacing: 1.6px;
    color: var(--band-ink);
    white-space: nowrap;
  }
</style>
</head>
<body>
<main class="sheet">

  <section class="card card-front" aria-label="Business card front">
    <div class="brand">
      <div class="brand-mark"></div>
      <div class="brand-rule"></div>
      <div class="brand-name">Carter Wells</div>
      <div class="brand-tag">PHOTOGRAPHERS</div>
    </div>
  </section>

  <section class="card card-back" aria-label="Business card back">
    <div class="brand">
      <div class="brand-mark"></div>
      <div class="brand-rule"></div>
      <div class="brand-name">Carter Wells</div>
      <div class="brand-tag">PHOTOGRAPHERS</div>
    </div>

    <div class="divider"></div>

    <ul class="contact-list">
      <li>
        <svg class="contact-icon" viewBox="0 0 18 18" aria-hidden="true">
          <circle cx="9" cy="9" r="8" fill="none" stroke="#cfcfcf" stroke-width="1.2"/>
          <path d="M6.2 5.2 L7.6 5 L8.3 6.9 L7.4 7.6 Q8.2 9.6 10.3 10.6 L11 9.7 L12.9 10.4 L12.7 11.8 Q8 12.4 6.2 5.2 Z" fill="#cfcfcf"/>
        </svg>
        <span>949.555.0142</span>
      </li>
      <li>
        <svg class="contact-icon" viewBox="0 0 18 18" aria-hidden="true"><circle cx="9" cy="9" r="8" fill="none" stroke="#cfcfcf" stroke-width="1.2"/><circle cx="9" cy="9" r="3" fill="#cfcfcf"/></svg>
        <span>social.example/CarterWellsPhoto</span>
      </li>
      <li>
        <svg class="contact-icon" viewBox="0 0 18 18" aria-hidden="true"><circle cx="9" cy="9" r="8" fill="none" stroke="#cfcfcf" stroke-width="1.2"/><circle cx="9" cy="9" r="3" fill="#cfcfcf"/></svg>
        <span>micro.example/CarterWells</span>
      </li>
      <li>
        <svg class="contact-icon" viewBox="0 0 18 18" aria-hidden="true">
          <circle cx="9" cy="9" r="8" fill="none" stroke="#cfcfcf" stroke-width="1.2"/>
          <rect x="5" y="6" width="8" height="6" fill="none" stroke="#cfcfcf" stroke-width="1"/>
          <path d="M5 6 L9 9.5 L13 6" fill="none" stroke="#cfcfcf" stroke-width="1"/>
        </svg>
        <span>carter@carterwells.com</span>
      </li>
      <li>
        <svg class="contact-icon" viewBox="0 0 18 18" aria-hidden="true">
          <circle cx="9" cy="9" r="8" fill="none" stroke="#cfcfcf" stroke-width="1.2"/>
          <circle cx="9" cy="9" r="4.2" fill="none" stroke="#cfcfcf" stroke-width="1"/>
          <path d="M4.8 9 H13.2 M9 4.8 V13.2" stroke="#cfcfcf" stroke-width="0.9"/>
        </svg>
        <span>www.carterwells.com</span>
      </li>
    </ul>

    <svg class="band" viewBox="0 0 900 120" aria-hidden="true">
      <path d="M0 0 H900 V120 H600 V60 H0 Z" fill="#d3d3d3"/>
      <path d="M0 60 H545 Q565 60 575 75 Q590 100 615 100 H900 V120 H0 Z" fill="#404042"/>
      <path d="M0 60 H545 Q565 60 575 75 Q590 100 615 100 H900" fill="none" stroke="#2f2f31" stroke-width="1"/>
    </svg>
    <div class="tagline">CALIFORNIA BASED WEDDING AND PORTRAIT PHOTOGRAPHER</div>
  </section>

</main>
</body>
</html>
```